IT solutions & services company requires stationary makeover

Looking for a consistent modern, professional design across our printed client touch points:
Business Cards
Letterhead
Client proposal
Flyer
Postcard

We provide solutions for SME IT - servers, backups, AV etc, and the ongoing services around them.
we are happy with our logo - please see attached and would like the colour theme to be maintained.

```html
<!DOCTYPE html>
<html lang="en">
<head>
<meta charset="utf-8">
<title>Corvane – Stationery Set</title>
<link href="https://fonts.googleapis.com/css2?family=Montserrat:wght@400;600;700&family=Open+Sans:wght@400;600&display=swap" rel="stylesheet">
<style>
  :root{
    --blue:#0a86bd;
    --blue-soft:#5fb4dc;
    --ink:#1b1b1b;
    --grey-text:#555;
    --paper:#ffffff;
    --stage:#e9eaec;
    --black-card:#0e0e0e;
  }
  *{box-sizing:border-box;margin:0;padding:0}
  html,body{width:1200px;height:795px;overflow:hidden}
  body{background:var(--stage);position:relative;font-family:"Open Sans",Arial,sans-serif;color:var(--ink)}

  .sheet{position:absolute;top:35px;width:360px;height:509px;background:var(--paper);overflow:hidden;box-shadow:0 2px 6px rgba(0,0,0,.15)}
  .card{position:absolute;top:590px;width:250px;height:143px;overflow:hidden;box-shadow:0 2px 5px rgba(0,0,0,.18)}

  /* brand lockup */
  .brand{display:flex;align-items:center;gap:7px}
  .brand-dot{width:16px;height:16px;border-radius:50%;background:var(--blue);flex:none}
  .brand-name{font-family:"Montserrat",Arial,sans-serif;font-weight:600;font-size:22px;line-height:1;color:var(--ink);letter-spacing:.5px}

  .contact-list{list-style:none;font-size:6px;line-height:1.7}
  .contact-list li{display:flex;align-items:center;gap:4px;white-space:nowrap}
  .contact-list li::before{content:"";width:4px;height:4px;background:var(--blue);flex:none}

  /* proposal cover */
  .proposal{left:30px}
  .proposal-band{position:absolute;left:0;top:0;width:100%;height:370px;background:var(--blue);overflow:hidden}
  .proposal-title{position:absolute;right:28px;top:210px;text-align:right;color:#fff}
  .proposal-title h1{font-family:"Montserrat",Arial,sans-serif;font-weight:700;font-size:22px}
  .proposal-title p{font-size:7px;margin-top:3px}
  .proposal-title .date{font-family:"Montserrat",Arial,sans-serif;font-size:13px;letter-spacing:2px;margin-top:18px}
  .proposal-foot{position:absolute;left:30px;right:24px;bottom:40px;display:flex;align-items:center;justify-content:flex-end;gap:12px}
  .proposal-foot .contact-list{border-left:1px solid var(--blue);padding-left:10px}

  /* letterhead */
  .letterhead{left:420px}
  .letterhead .brand{position:absolute;left:26px;top:32px}
  .letterhead-sender{position:absolute;right:24px;top:30px;display:flex;gap:8px;align-items:flex-start}
  .sender-name{font-family:"Montserrat",Arial,sans-serif;font-weight:600;font-size:10px;color:var(--blue);text-align:right}
  .sender-role{font-size:6px;color:var(--grey-text);text-align:right}
  .letterhead-sender .contact-list{border-left:1px solid var(--blue);padding-left:7px;font-size:5.5px}
  .wave{position:absolute;left:0;bottom:0;width:100%;height:100%}

  /* flyer */
  .flyer{left:810px;padding:38px 30px 0}
  .flyer h2{font-family:"Montserrat",Arial,sans-serif;font-weight:700;font-size:20px;color:var(--blue);text-align:right}
  .flyer .sub{font-size:7px;text-align:right;color:var(--grey-text);margin-bottom:22px}
  .flyer p.body{font-size:8px;line-height:1.55;margin-bottom:10px;color:#222;text-align:justify}
  .flyer .brand{position:absolute;right:30px;bottom:76px}
  .flyer-rule{position:absolute;left:30px;right:30px;bottom:56px;height:1.5px;background:var(--blue)}
  .flyer-footer{position:absolute;left:30px;right:30px;bottom:38px;display:flex;justify-content:space-between;list-style:none;font-size:6px}
  .flyer-footer li{display:flex;align-items:center;gap:4px}
  .flyer-footer li::before{content:"";width:4px;height:4px;background:var(--blue)}

  /* business cards */
  .card-front{background:var(--paper)}
  .card-front .brand{position:absolute;left:22px;top:36px}
  .card-front.plain .brand{top:60px;left:34px}
  .card-back{padding:22px 20px 0 118px;color:#fff}
  .card-back.dark{background:var(--black-card)}
  .card-back.blue{background:var(--blue)}
  .card-back .sender-name{text-align:left;font-size:12px}
  .card-back.dark .sender-name{color:var(--blue-soft)}
  .card-back.blue .sender-name{color:#fff}
  .card-back .sender-role{text-align:left;color:#ddd;margin-bottom:12px}
  .card-back .contact-list{font-size:6.5px;color:#fff}
  .card-back.blue .contact-list li::before{background:#fff}
  .card-back .brand{position:absolute;left:18px;top:62px}
  .card-back .brand-name{font-size:16px;color:#fff}
  .card-back .brand-dot{width:11px;height:11px}
  .card-back.blue .brand-dot{background:#fff}
</style>
</head>
<body>

  <!-- Proposal cover -->
  <section class="sheet proposal">
    <div class="proposal-band">
      <div class="proposal-title">
        <h1>Company Overview</h1>
        <p>IT services proposal for growing teams</p>
        <p class="date">August 2014</p>
      </div>
    </div>
    <div class="proposal-foot">
      <div class="brand">
        <span class="brand-dot"></span>
        <span class="brand-name">corvane</span>
      </div>
      <ul class="contact-list">
        <li>+1 555 014 2880</li>
        <li>hello@corvane-it.net</li>
        <li>48 Harbour Lane, Kestrel City</li>
      </ul>
    </div>
  </section>

  <!-- Letterhead -->
  <section class="sheet letterhead">
    <svg class="wave" viewBox="0 0 360 509" preserveAspectRatio="none" aria-hidden="true">
      <path d="M0,509 L0,500 C130,478 255,425 318,345 C338,318 352,290 360,268 L360,509 Z" fill="var(--blue)"/>
      <path d="M0,486 C140,462 262,410 338,310 C280,400 150,468 0,496 Z" fill="var(--ink)"/>
    </svg>
    <div class="brand">
      <span class="brand-dot"></span>
      <span class="brand-name">corvane</span>
    </div>
    <div class="letterhead-sender">
      <div>
        <div class="sender-name">Elias Marlow</div>
        <div class="sender-role">Managing Director</div>
      </div>
      <ul class="contact-list">
        <li>+1 555 014 2880</li>
        <li>hello@corvane-it.net</li>
        <li>48 Harbour Lane, Kestrel City</li>
      </ul>
    </div>
  </section>

  <!-- Flyer -->
  <section class="sheet flyer">
    <h2>Sample Text</h2>
    <p class="sub">Managed IT support for small business</p>
    <p class="body">Our team keeps small offices running with reliable servers, tested backups and clear support plans. We plan each upgrade around your working day, document every change and stay on hand when questions come up.</p>
    <p class="body">From meeting room screens to remote access, we set up the tools your staff use daily and look after them with regular health checks, patching and honest advice about what to replace next.</p>
    <p class="body">Every client has one named contact who knows their systems well. Monthly reports show what was done, what is planned and where budget is best spent over the coming year.</p>
    <p class="body">Talk to us about a simple review of your current setup and a plan that grows with you.</p>
    <div class="brand">
      <span class="brand-dot"></span>
      <span class="brand-name">corvane</span>
    </div>
    <div class="flyer-rule"></div>
    <ul class="flyer-footer">
      <li>+1 555 014 2880</li>
      <li>www.corvane-it.net</li>
      <li>48 Harbour Lane, Kestrel City</li>
    </ul>
  </section>

  <!-- Business cards -->
  <section class="card card-front plain" style="left:55px">
    <div class="brand">
      <span class="brand-dot"></span>
      <span class="brand-name">corvane</span>
    </div>
  </section>

  <section class="card card-back dark" style="left:335px">
    <div class="brand">
      <span class="brand-dot"></span>
      <span class="brand-name">corvane</span>
    </div>
    <div class="sender-name">Elias Marlow</div>
    <div class="sender-role">Managing Director</div>
    <ul class="contact-list">
      <li>+1 555 014 2880</li>
      <li>hello@corvane-it.net</li>
      <li>www.corvane-it.net</li>
      <li>48 Harbour Lane, Kestrel City</li>
    </ul>
  </section>

  <section class="card card-front" style="left:615px">
    <svg class="wave" viewBox="0 0 250 143" preserveAspectRatio="none" aria-hidden="true">
      <path d="M0,143 L0,128 C90,118 180,105 225,80 C238,72 246,62 250,55 L250,143 Z" fill="var(--blue)"/>
      <path d="M0,118 C95,108 190,95 240,62 C200,92 100,112 0,124 Z" fill="var(--ink)"/>
    </svg>
    <div class="brand">
      <span class="brand-dot"></span>
      <span class="brand-name">corvane</span>
    </div>
  </section>

  <section class="card card-back blue" style="left:895px">
    <div class="brand">
      <span class="brand-dot"></span>
      <span class="brand-name">corvane</span>
    </div>
    <div class="sender-name">Elias Marlow</div>
    <div class="sender-role">Managing Director</div>
    <ul class="contact-list">
      <li>+1 555 014 2880</li>
      <li>hello@corvane-it.net</li>
      <li>www.corvane-it.net</li>
      <li>48 Harbour Lane, Kestrel City</li>
    </ul>
  </section>

</body>
</html>
```